Mobile Repair Service on location needs a Web Design

We are starting a new mobile device repair service called Cell Revive and our website needs a design!

Hello Designers!
First, we'd like to make clear this is more than a simple web design contest, we want the designers to create an idea. We want someone who can create the whole theme of the service's we provide. We want someone that can help design our visual branding, help us communicate a sentiment. And we are willing to pay for that.

Who are we?
Our company is based in Rotterdam, the Netherlands. We provide different services for all kinds of electronic devices. The kind of services we provide are, among other things, installations of hardware and software and the repair of broken or malfunctioning devices.
We are starting a new service that offers mobile device repairs on location, be it at the home of our customers, their office, or any other place. Just give us the address and we will come to you for the repair job. This is also our main USP. We have multiple skilled engineers who drive trough the country on a daily basis and can be on location within a working day. Repair is done immediately onsite while the customer waits. At this stage we will start with the smartphone product-group within the mobile devices. In a second phase we might also add tablets.
People don't want to be without their phone for weeks because of some parts that needed to be ordered by a repair center they had to sent their phone to. We offer a fully functional mobile repair center in the form of specially customized vans. These vans have all the tools and utilities needed by our engineers to safely repair your mobile device. Your phone is being repaired directly in front of you, the next business-day, on a location you desire.

For this new service we are creating a website called Cell Revive. The website needs a story and matching design and this is where you come in. We are not looking for a simple template design we can get from any place. We need a story. We want you to create an idea, build a unique theme or vision that helps sell the product/service. This goes beyond the design of the website. We need the whole package, the design you are creating needs to have returning elements like icons, color use, images, maybe even characters etc. You name it! There needs to be a common thread in the design so we can reuse elements in, for example, the email templates, the work order or receipt we give to our customers (we may contact the winner of the contest to design these for us as well!).

The name 'Cell Revive' is chosen. Revive (short for rehabilitate) has a bold and playful tone to it and the design needs to reflect the name. So we're looking for a somewhat playful and cheeky design. Definitely not too serious and definitely modern. We already got a logo that we love and that fit's this description (see attached design documents for the logo). It's bold, powerful and fun. Our web design needs to reflect this as well and has to fit in with our logo.
We would really like it if the design somehow incorporates elements that highlight our unique selling points (repairs on location, we come to you etc.). We would really like some form of story telling in the design. Think clumsy people breaking their phones. Teenagers in tears because they have no access to their friends. People nowadays have the need to always be 'connected'. What happens when your phone is broken or malfunctioning? We're handling tech, we are nerds and a little bit weird, but we're professionals and here to help you with your problem. The sentiment Byte Troop tries to communicate is something we really like. We're looking for fresh idea's, anything goes!

In an overview all Unique Selling Points of the Cell revive service:
- Professional service on location. Don’t ship to us we will come to you!
- Clear pricing upfront. No hidden cost.
- Next business-day repair.
- Backed by a professional call center open 12 hours a day and open on a Saturday as well
- Backed by a professional repair center with more then 12 years of experience
- Repair is done by certified engineers
- 1 year warranty on the repair

The process:
The main function of our website will be for customers to make a repair request. A customer will visit our website and can make a repair request immediately by going through a 'request-order-flow'. In this flow he or she will need to fill in some forms and can select wich type/model/brand of mobile device he or she has and what parts need to be repaired. After a request is placed we will call the customer back (within an hour) for a short intake and to set a date/time and location. Our engineer will meet the customer at the specified location and will repair the device onsite in one of our mobile repair centers, which is a specialized van equipped with all the tools needed for device restorations.
So in short the steps are:
- Choose your device and repair job
- Place the order
- Get a callback within the hour
- Set date and location
- We will come to you.

Website functionality:
Our website is our main form of communication. So the sentiment we want to communicate needs be reflected in the design. We need a main/front page designed (preferably a long scrolling page design) containing:
1. Customers will be able to request a repair job directly on our website. So there will need to be a prominent button/link at the top of our main page that will bring the customer to this 'request-order-flow'. This is the main flow which needs to be full focus on the front page. All other items are secondary.
2. The general information of who we are and what we do, and why the customer should choose us. Preferably in short bullet-point type keywords/sentences with icons or other visual cues. See our unique selling points to get an idea of the information that will be displayed here.
3. There needs to be a section that will explain the process (see above) of a repair request step-by- step, again in brief short key sentences and with (custom) icons.
4. There needs to be a section that explains to the customer he/she can always contact us if they are not sure what the problem is with their device, and for this reason are not sure what repair request they should order.
5. We want to implement some functionality that display customer ratings or customer reviews. So there needs to be room for some kind of widget of plugin we're going to implement which shows these reviews.
6. A 'For business section' where we will explain all the options we provide for corporate clients.
7. Social media links.
8. There needs to be a menu with buttons that leads to the all sections described in the previous points.

For now, we need a design for our front page. In the second phase, when we have picked our winner, we may ask the winner to design the page(s) for our request workflow as well.

EDIT:
Finally, we have a very specific order in mind for the different segments of our website. We would like you to add some more segments that were not in our original brief as well:

1. Top header with order/request button. (should instantly make clear our main USP, we do repairs on location)
2. Our process
3. Our unique selling points / why choose us
4. The kind of repairs we do (broken screens, broken batteries, water damage, broken camera's, no sound etc.)
5. A 'meet our team' section, where we introduce some of our engineers
6. A 'contact us for any questions' section/
7. Testimonials/user reviews
8. A section where we show key performance indicators
9. 'For businesses' sections
10.'Subscribe for newsletter' field
11. Social media buttons
Updates

Industry/Entity Type

It Service

Number of Pages Required

1 page

Font styles to use
Sans Serif

Requirements
Must have
• a main/front page, design only
• custom icons/images for banners, adverts online and in print (high res)
Nice to have
• Storytelling in our design.
• Design that fits with our brand new logo.
• Elements like icons to have a flat design.
• Keep in mind that the website will need to be responsive when designing! (Ideally provide an example of the mobile design as well)
• Create a fun and trustworthy feeling.

```html
<!DOCTYPE html>
<html lang="en">
<head>
<meta charset="utf-8">
<title>Cell Revive – We will come to you</title>
<link href="https://fonts.googleapis.com/css2?family=Oswald:wght@400;500;600&family=Raleway:ital,wght@0,400;0,500;0,600;0,700;1,400;1,500&display=swap" rel="stylesheet">
<style>
:root{
  --yellow:#f6e24a;
  --yellow-deep:#f2cf2a;
  --navy:#1b2335;
  --orange:#e8562a;
  --orange-deep:#d3441d;
  --red:#e0322a;
  --green:#8cc63f;
  --blue:#3aa6df;
  --brown:#b0784a;
  --grey-bg:#e7e8e9;
  --ink:#222;
  --white:#fff;
  --footer:#2a2a2a;
}
*{box-sizing:border-box;margin:0;padding:0}
html,body{width:1200px;height:3607px;overflow:hidden}
body{font-family:"Raleway",sans-serif;color:var(--ink);position:relative;background:#fff}
.section{position:absolute;left:0;width:1200px;overflow:hidden}
.heading{font-family:"Oswald",sans-serif;text-transform:uppercase;letter-spacing:1px}
.center{position:absolute;left:0;width:100%;text-align:center}

/* hero */
.hero{top:0;height:577px;background:radial-gradient(ellipse at 50% 40%,#fbec6a 0%,var(--yellow) 55%,var(--yellow-deep) 100%)}
.brand{position:absolute;left:232px;top:22px;display:flex;align-items:center;gap:12px;background:#fff;border-radius:40px;padding:14px 22px 14px 14px;z-index:2}
.brand-dot{width:46px;height:46px;border-radius:50%;background:var(--orange)}
.brand-name{font-family:"Raleway",sans-serif;font-weight:700;font-size:26px;color:var(--navy);line-height:1}
.nav{position:absolute;left:664px;top:26px;display:flex;gap:16px;font-family:"Oswald",sans-serif;font-size:13px;color:var(--ink);text-transform:uppercase;z-index:2}
.nav-cta{position:absolute;left:1048px;top:19px;width:130px;height:30px;border-radius:15px;background:var(--red);color:#fff;font-family:"Oswald",sans-serif;font-size:13px;line-height:30px;text-align:center;text-transform:uppercase;z-index:2}
.char-left{position:absolute;left:0;top:0;width:262px;height:577px;
  background:radial-gradient(ellipse 70% 30% at 35% 22%,#f0c7a2 0%,rgba(240,199,162,.8) 55%,rgba(240,199,162,0) 100%),
             radial-gradient(ellipse 90% 55% at 40% 85%,#3b4150 0%,rgba(59,65,80,.75) 55%,rgba(59,65,80,0) 100%);
  -webkit-mask-image:linear-gradient(90deg,#000 70%,transparent 100%);mask-image:linear-gradient(90deg,#000 70%,transparent 100%)}
.char-right{position:absolute;left:880px;top:30px;width:300px;height:547px;
  background:radial-gradient(ellipse 55% 26% at 50% 22%,#f0c7a2 0%,rgba(240,199,162,.8) 55%,rgba(240,199,162,0) 100%),
             radial-gradient(ellipse 85% 55% at 50% 80%,#4cae4f 0%,rgba(76,174,79,.75) 55%,rgba(76,174,79,0) 100%);
  -webkit-mask-image:linear-gradient(270deg,#000 75%,transparent 100%);mask-image:linear-gradient(270deg,#000 75%,transparent 100%)}
.hero-title{top:152px;font-size:36px;line-height:48px;color:var(--ink);font-weight:500}
.hero-rule{position:absolute;left:400px;top:212px;width:400px;height:3px;background:var(--red)}
.believe{top:240px;font-family:"Oswald",sans-serif;font-size:30px;line-height:40px;color:var(--navy);text-transform:uppercase;letter-spacing:2px}
.believe-sub{top:284px;font-family:"Oswald",sans-serif;font-size:24px;line-height:32px;color:var(--red);text-transform:uppercase;letter-spacing:1px}
.hero-lines{top:322px;font-family:"Oswald",sans-serif;font-size:22px;line-height:27px;color:var(--red);text-transform:uppercase;letter-spacing:1px}
.scroll-label{top:444px;font-size:13px;font-weight:600;text-transform:uppercase;color:var(--ink)}
.scroll-rule{position:absolute;left:530px;top:466px;width:140px;height:1px;background:var(--ink)}
.scroll-arrow{position:absolute;left:560px;top:478px}

/* story */
.story{top:577px;height:577px}
.story-scene{position:absolute;inset:0;background:linear-gradient(180deg,#151b2a 0%,#243043 55%,#2f6a68 80%,#1d2c36 100%)}
.story-title{top:56px;font-size:40px;line-height:56px;color:var(--yellow);font-weight:500}
.story-divider{position:absolute;left:560px;top:124px;width:80px;height:1px;background:var(--yellow)}
.story-kicker{top:160px;font-size:15px;font-weight:600;color:var(--yellow);text-transform:uppercase;letter-spacing:1px}
.story-sub{top:196px;font-family:"Oswald",sans-serif;font-size:26px;line-height:36px;color:var(--green);text-transform:uppercase;letter-spacing:1px}
.story-text{position:absolute;left:385px;top:290px;width:445px;text-align:center;color:#fff;font-size:15px;line-height:26px}
.story-quote{top:440px;font-family:"Oswald",sans-serif;font-size:40px;color:var(--yellow);line-height:1}
.dots{position:absolute;display:flex;gap:8px}
.dots span{width:9px;height:9px;border-radius:50%;background:rgba(255,255,255,.55)}
.dots span.on{background:#fff}

/* usp */
.usp{top:1154px;height:679px;background:linear-gradient(180deg,var(--orange) 0%,#ec6a34 100%)}
.usp-title{top:42px;font-size:21px;line-height:34px;color:#fff}
.read-more{position:absolute;left:1073px;top:53px;width:101px;height:24px;border-radius:12px;background:var(--yellow);color:var(--orange-deep);font-size:10px;font-weight:700;line-height:24px;text-align:center;text-transform:uppercase}
.usp-rule{position:absolute;left:392px;top:132px;width:414px;height:1px;background:rgba(255,255,255,.8)}
.usp-rule::after{content:"";position:absolute;left:201px;top:-4px;width:9px;height:9px;border-radius:50%;background:var(--navy)}
.usp-card{position:absolute;width:275px;height:155px;border:1px solid rgba(255,255,255,.85);color:#fff;text-align:center;font-size:13px;line-height:19px;padding:70px 14px 0}
.usp-icon{position:absolute;left:94px;top:-43px;width:86px;height:86px;border-radius:50%;border:4px solid #fff;display:flex;align-items:center;justify-content:center;box-shadow:0 3px 6px rgba(0,0,0,.18)}
.usp-icon svg{width:44px;height:44px;fill:none;stroke:#fff;stroke-width:2.6;stroke-linecap:round;stroke-linejoin:round}

/* help */
.help{top:1833px;height:577px;background:linear-gradient(180deg,#d7461f 0%,#e2582b 100%)}
.help-art{position:absolute;left:0;top:60px;width:470px;height:517px;
  background:radial-gradient(ellipse 40% 22% at 45% 18%,#f3efe9 0%,rgba(243,239,233,.6) 60%,rgba(243,239,233,0) 100%),
             radial-gradient(ellipse 55% 50% at 40% 70%,#e34c3c 0%,rgba(227,76,60,.6) 60%,rgba(227,76,60,0) 100%),
             radial-gradient(ellipse 60% 22% at 30% 95%,#e9c93a 0%,rgba(233,201,58,0) 100%)}
.help-title{position:absolute;left:512px;top:54px;width:620px;font-size:25px;line-height:36px;color:#fff;font-weight:500}
.help-note{position:absolute;left:512px;top:148px;width:560px;font-style:italic;font-size:16px;line-height:27px;color:#7fc4ef}
.steps{position:absolute;left:524px;top:224px;list-style:none}
.step{display:flex;align-items:center;height:48px;margin-bottom:21px;color:#fff;font-size:17px}
.step-num{width:48px;height:48px;border-radius:50%;border:3px solid rgba(255,255,255,.85);color:#fff;font-family:"Oswald",sans-serif;font-size:22px;line-height:42px;text-align:center;margin-right:22px}
.n1{background:var(--orange)}.n2{background:#f2cf2a}.n3{background:var(--blue)}.n4{background:var(--green)}.n5{background:var(--brown)}
.help-cta{position:absolute;left:1000px;top:490px;width:174px;height:46px;border-radius:23px;background:var(--blue);color:#fff;font-size:13px;font-weight:700;line-height:46px;text-align:center;text-transform:uppercase}

/* reviews */
.reviews{top:2410px;height:577px;background:var(--grey-bg)}
.reviews-title{top:50px;font-size:26px;color:var(--orange);font-weight:500}
.reviews-rule{position:absolute;top:131px;height:1px;width:270px;background:#2a7f83}
.quote-dot{position:absolute;left:578px;top:110px;width:43px;height:43px;border-radius:50%;background:var(--orange);color:#fff;font-family:"Oswald",sans-serif;font-size:30px;line-height:50px;text-align:center}
.avatar{position:absolute;left:125px;top:219px;width:184px;height:184px;border-radius:50%;border:5px solid #fff;background:linear-gradient(180deg,#c9b8a6 0%,#8a7a6c 55%,#2f3a4c 100%)}
.stars{position:absolute;left:125px;top:432px;width:184px;text-align:center;color:#f4b400;font-size:20px;letter-spacing:2px}
.reviewer{position:absolute;left:100px;top:462px;width:234px;text-align:center;font-size:14px;font-weight:700;text-transform:uppercase}
.reviewer-role{position:absolute;left:100px;top:490px;width:234px;text-align:center;font-size:11px;font-weight:600;color:var(--orange);text-transform:uppercase}
.review-text{position:absolute;left:380px;top:280px;width:555px;font-style:italic;font-size:16px;line-height:27px;color:#444}

/* newsletter */
.newsletter{top:2987px;height:577px}
.party-photo{position:absolute;inset:0;background:
  radial-gradient(circle at 22% 18%,#5fa9d6 0%,rgba(95,169,214,0) 22%),
  radial-gradient(circle at 80% 12%,#f1cc3b 0%,rgba(241,204,59,0) 20%),
  linear-gradient(120deg,#e8a44a 0%,#b5532c 35%,#6a2a1c 65%,#c8703c 100%)}
.news-title{top:138px;font-size:13px;font-weight:700;color:var(--ink);text-transform:uppercase;letter-spacing:1px}
.news-field{position:absolute;left:356px;top:178px;width:491px;height:53px;border-radius:27px;background:#fff;font-size:12px;color:#888;padding:0 26px;line-height:53px}
.news-send{position:absolute;right:22px;top:18px}
.link-pill{position:absolute;left:447px;top:351px;width:306px;height:32px;border-radius:16px;background:#111;display:flex;justify-content:center;align-items:center;gap:22px;color:#fff;font-size:12px;font-weight:700;text-transform:uppercase;letter-spacing:1px}
.social{position:absolute;top:443px;width:54px;height:54px;border-radius:50%;background:#fff}

/* footer */
.footer{top:3564px;height:43px;background:var(--footer);color:#9a9a9a;font-size:10px}
.footer-copy{position:absolute;left:40px;top:15px}
.footer-links{position:absolute;right:30px;top:15px;display:flex;gap:16px}
</style>
</head>
<body>

<header class="section hero">
  <div class="char-left" role="img" aria-label="Illustration of a puzzled man in a suit holding his chin"></div>
  <div class="char-right" role="img" aria-label="Illustration of a smiling engineer in a green shirt with arms crossed"></div>
  <div class="brand"><span class="brand-dot"></span><span class="brand-name">Cell Revive</span></div>
  <nav class="nav"><span>Home</span><span>About us</span><span>Why us</span><span>How we work</span><span>Contact</span></nav>
  <div class="nav-cta">Request a repair</div>
  <h1 class="center heading hero-title">Don't ship to us we will come to you</h1>
  <div class="hero-rule"></div>
  <p class="center believe">Believe</p>
  <p class="center believe-sub">It or not</p>
  <p class="center hero-lines">We will repair your broken<br>smart phones at your place<br>at your time</p>
  <p class="center scroll-label">Scroll for more</p>
  <div class="scroll-rule"></div>
  <svg class="scroll-arrow" width="80" height="82" viewBox="0 0 80 82">
    <path d="M6 6 H74 L40 76 Z" fill="#fff" stroke="#1b2335" stroke-width="4" stroke-linejoin="round"/>
    <path d="M28 26 L40 40 L52 26" fill="none" stroke="#1b2335" stroke-width="5" stroke-linecap="round" stroke-linejoin="round"/>
  </svg>
</header>

<section class="section story">
  <div class="story-scene" role="img" aria-label="Night scene in the rain with a man reading his cracked phone beside an iron fence and trees"></div>
  <h2 class="center heading story-title">A short story of Tim</h2>
  <div class="story-divider"></div>
  <p class="center story-kicker">You will love to see it</p>
  <p class="center story-sub">How we work</p>
  <p class="story-text">Tim is a creative director to an additional agency. One rainy night while returning home his phone got a fall from his hand and the front screen shattered. Somehow he managed to go home that night, but he was upset with the phone</p>
  <p class="center story-quote">&rdquo;</p>
  <div class="dots" style="left:556px;top:525px"><span class="on"></span><span></span><span></span><span></span><span></span><span></span></div>
</section>

<section class="section usp">
  <h2 class="center heading usp-title">Our experts literally<br>thrives to satisfy our customers</h2>
  <div class="read-more">Read more</div>
  <div class="usp-rule"></div>

  <div class="usp-card" style="left:26px;top:222px"><span class="usp-icon" style="background:#5fb7e5"><svg viewBox="0 0 40 40" aria-hidden="true"><path d="M7 20 L20 9 L33 20"/><path d="M11 17 V32 H29 V17"/><path d="M17 32 V24 H23 V32"/></svg></span>Professional service on location.<br>Don't ship to us we will come to you</div>
  <div class="usp-card" style="left:320px;top:222px"><span class="usp-icon" style="background:#e45a2b"><svg viewBox="0 0 40 40" aria-hidden="true"><path d="M8 8 H20 L33 21 L21 33 L8 20 Z"/><circle cx="14" cy="14" r="2"/></svg></span>Clear pricing upfront.<br>No hidden cost</div>
  <div class="usp-card" style="left:613px;top:222px"><span class="usp-icon" style="background:#8cc63f"><svg viewBox="0 0 40 40" aria-hidden="true"><rect x="8" y="10" width="24" height="22" rx="2"/><path d="M8 17 H32 M14 7 V12 M26 7 V12 M15 24 L19 28 L26 21"/></svg></span>Next business-day repair</div>
  <div class="usp-card" style="left:904px;top:222px"><span class="usp-icon" style="background:#d7342a"><svg viewBox="0 0 40 40" aria-hidden="true"><path d="M10 23 V20 A10 10 0 0 1 30 20 V23"/><rect x="8" y="22" width="5" height="9" rx="2"/><rect x="27" y="22" width="5" height="9" rx="2"/><path d="M30 31 C30 34 26 34 22 34"/></svg></span>Backed by a professional call center</div>

  <div class="usp-card" style="left:26px;top:467px"><span class="usp-icon" style="background:#f2cf2a"><svg viewBox="0 0 40 40" aria-hidden="true"><path d="M12 8 H28 M12 32 H28"/><path d="M14 8 C14 16 26 16 26 20 C26 24 14 24 14 32"/><path d="M26 8 C26 16 14 16 14 20 C14 24 26 24 26 32"/></svg></span>Open 12 hours a day and open on a<br>Saturday as well</div>
  <div class="usp-card" style="left:320px;top:467px"><span class="usp-icon" style="background:#3e8e7e"><svg viewBox="0 0 40 40" aria-hidden="true"><rect x="13" y="6" width="14" height="28" rx="2.5"/><path d="M18 29 H22 M16 12 L24 20 M22 12 L17 19"/></svg></span>Backed by a professional repair center<br>with more then 12 years of experience</div>
  <div class="usp-card" style="left:613px;top:467px"><span class="usp-icon" style="background:#2f4f8f"><svg viewBox="0 0 40 40" aria-hidden="true"><circle cx="20" cy="20" r="13"/><path d="M13 20 L18 25 L27 15"/></svg></span>Repair is done by certified engineers</div>
  <div class="usp-card" style="left:904px;top:467px"><span class="usp-icon" style="background:#2e7a70"><svg viewBox="0 0 40 40" aria-hidden="true"><path d="M20 6 L31 10 V19 C31 26 26 31 20 34 C14 31 9 26 9 19 V10 Z"/><path d="M15 20 L19 24 L26 16"/></svg></span>1 year warranty on the repair</div>
</section>

<section class="section help">
  <div class="help-art" role="img" aria-label="Illustration of an elderly woman holding a phone beside a bed and lamp"></div>
  <h2 class="heading help-title">Hmmm... you can't detect why your phone is shutting down spontaneously for last few days...</h2>
  <p class="help-note">We know you are not technical, no worries, our Engineers will detect it. Just follow these 5 easy steps</p>
  <ol class="steps">
    <li class="step"><span class="step-num n1">1</span>Open cellrevive.com</li>
    <li class="step"><span class="step-num n2">2</span>Click request a repair</li>
    <li class="step"><span class="step-num n3">3</span>Wait for a call</li>
    <li class="step"><span class="step-num n4">4</span>Our PRO will call you</li>
    <li class="step"><span class="step-num n5">5</span>Book a time</li>
  </ol>
  <div class="help-cta">Request a repair</div>
</section>

<section class="section reviews">
  <h2 class="center heading reviews-title">We don't say but our customers rated us in an average 5.</h2>
  <div class="reviews-rule" style="left:290px"></div>
  <div class="reviews-rule" style="left:640px"></div>
  <div class="quote-dot">&rdquo;</div>
  <div class="avatar" role="img" aria-label="Portrait photo of the reviewer"></div>
  <div class="stars">★★★★★</div>
  <p class="reviewer">Maren Holt</p>
  <p class="reviewer-role">CEO, Lumen Works</p>
  <p class="review-text">Lorem ipsum dolor sit amet, consectetur adipiscing elit, sed do eiusmod tempor incididunt ut labore et dolore magna aliqua. Ut enim ad minim veniam, quis nostrud exercitation ullamco laboris nisi ut aliquip ex ea commodo consequat. Duis aute irure dolor in reprehenderit in voluptate velit esse cillum dolore eu fugiat nulla pariatur.</p>
  <div class="dots" style="left:504px;top:496px"><span class="on" style="background:var(--orange)"></span><span style="background:#f1a58a"></span><span style="background:#f1a58a"></span><span style="background:#f1a58a"></span></div>
</section>

<section class="section newsletter">
  <div class="party-photo" role="img" aria-label="Photo of friends celebrating with balloons and drinks against a brick wall"></div>
  <p class="center news-title">Being in the know feels great</p>
  <div class="news-field">Signup For latest news and updates from us
    <svg class="news-send" width="18" height="18" viewBox="0 0 18 18"><path d="M1 8 L17 1 L11 17 L8 10 Z" fill="none" stroke="#333" stroke-width="1.5" stroke-linejoin="round"/></svg>
  </div>
  <div class="link-pill"><span>Locate us</span><span>|</span><span>Request a repair</span></div>
  <span class="social" style="left:502px" role="img" aria-label="Social link"></span>
  <span class="social" style="left:573px" role="img" aria-label="Social link"></span>
  <span class="social" style="left:644px" role="img" aria-label="Social link"></span>
</section>

<footer class="section footer">
  <span class="footer-copy">Copyright Message</span>
  <div class="footer-links"><span>Home</span><span>About Us</span><span>Why Us</span><span>How We Work</span><span>Request a Repair</span><span>Terms &amp; Conditions</span><span>Privacy Policy</span><span>Contact Us</span></div>
</footer>

</body>
</html>
```